Haskell and Dunmore Ranch Insurance

Would like you all to design a logo for our Business cards and possible letterhead.
This business provides Ranch insurance for folks in Texas, New Mexico, and Oklahoma

Ggood stuff everybody, be sure to include email and Mobil for both of us on all designs

Thanks

Hello All

Wanted to let you all know i am going to extend deadline a few days, and add some more $$ to the budget

Reason: Give everybody a bit ,more time, and I added more money

Appreciate all of yalls hard work, will review and provide feed back hopefully today, been a little whacky with the holidays and all

```html
<!DOCTYPE html>
<html lang="en">
<head>
<meta charset="utf-8">
<title>Haskell and Dunmore – Business Card</title>
<link rel="stylesheet" href="https://fonts.googleapis.com/css2?family=Questrial&display=swap">
<style>
  :root {
    --page-bg: #ffffff;
    --card-dark: #1e1f20;
    --card-mid: #2c2d2f;
    --frame-light: #f2f2f2;
    --frame-dark: #8a8a8a;
    --accent-red: #e0222a;
    --text-white: #ffffff;
  }
  * { margin: 0; padding: 0; box-sizing: border-box; }
  html, body {
    width: 1200px; height: 900px; overflow: hidden;
    background: var(--page-bg);
    font-family: "Questrial", "Century Gothic", sans-serif;
  }
  .business-card {
    position: absolute; left: 100px; top: 142px;
    width: 1000px; height: 616px;
    background: radial-gradient(ellipse at 50% 40%, var(--card-mid), var(--card-dark) 75%);
    color: var(--text-white);
  }
  .card-frame {
    position: absolute; left: 21px; top: 21px; right: 21px; bottom: 21px;
    border: 5px solid var(--frame-light);
    border-image: linear-gradient(135deg, var(--frame-dark), var(--frame-light) 30%, var(--frame-dark) 55%, var(--frame-light) 80%, var(--frame-dark)) 1;
  }
  .contact-person { position: absolute; top: 58px; font-size: 23px; line-height: 32px; }
  .contact-person--left { left: 54px; }
  .contact-person--right { right: 54px; text-align: right; }
  .contact-person .person-name { color: var(--accent-red); font-size: 29px; line-height: 40px; }
  .brand-name {
    position: absolute; left: 0; right: 0; top: 226px;
    text-align: center; color: var(--accent-red);
    font-size: 52px; letter-spacing: 1px;
  }
  .office-details { position: absolute; left: 54px; top: 412px; font-size: 26px; line-height: 36px; }
  .office-line { display: flex; align-items: center; gap: 8px; }
  .office-line svg { width: 32px; height: 32px; flex: none; }
  .office-line--indent { padding-left: 40px; }
  .office-line--web { margin-top: 4px; }
</style>
</head>
<body>
  <section class="business-card">
    <div class="card-frame"></div>

    <div class="contact-person contact-person--left">
      <p class="person-name">Wade Haskell</p>
      <p>haskellw@ranvo.com,</p>
      <p>cell # 512-555-0147</p>
    </div>

    <div class="contact-person contact-person--right">
      <p class="person-name">Roy Dunmore</p>
      <p>roy@haskellanddunmore.com</p>
      <p>cell #325-555-0186</p>
    </div>

    <p class="brand-name">Haskell and Dunmore</p>

    <div class="office-details">
      <p class="office-line">
        <svg viewBox="0 0 24 24" aria-hidden="true"><path fill="#e0222a" d="M6.6 3.2c.6-.6 1.6-.6 2.1 0l2.3 2.7c.5.6.5 1.4 0 2l-1.5 1.6c1 2.2 2.8 4 5 5l1.6-1.5c.6-.5 1.4-.5 2 0l2.7 2.3c.6.5.6 1.5 0 2.1l-1.5 1.6c-.8.8-2.1 1.1-3.2.7C10.600 17.300 6.700 13.400 4.300 7.900c-.4-1.100-.1-2.400.7-3.200z"/></svg>
        325.555.0129
      </p>
      <p class="office-line">
        <svg viewBox="0 0 24 24" aria-hidden="true"><path fill="#e0222a" d="M12 3 1.5 12h3v9h5.5v-6h4v6H19.5v-9h3z"/></svg>
        418 W Oak St.
      </p>
      <p class="office-line office-line--indent">Eldorado, TX 76936</p>
      <p class="office-line office-line--web">
        <svg viewBox="0 0 24 24" aria-hidden="true"><g fill="none" stroke="#e0222a" stroke-width="1.8"><circle cx="12" cy="12" r="9.5"/><ellipse cx="12" cy="12" rx="4.2" ry="9.5"/><path d="M2.5 12h19M4 7h16M4 17h16M12 2.5v19"/></g></svg>
        www.haskellanddunmore.com
      </p>
    </div>
  </section>
</body>
</html>
```